Drinking Game needs a revamped look!

** Please note we are looking for a redesign of the actual game board, not a poster about the game. I chose poster because it was the closest description of what we need. If you have questions, please ask prior to starting.

We need a new look for our Tip Tumble drinking game. I have attached the old tired graphic we use for our games. We want to liven it up a bit! Along with revamping the current look of the game we are also adding Tip "a wee" tumble as a cheaper alternative. We will need a design for that as well. Both can be about the same size of about 11.5x17.5". The difference on the tip a wee tumble will be one less number and one less letter so A-I and 1-7.

I have also attached our current logo which I would like incorporated in the design as well as our site TipTumble.com.
Updates

Target Market(s)

Drinkers and game players :-)

Requirements
Must have
• A hot new look that stands out from stained wood. You can see the current product at www.tiptumble.com.

```html
<!DOCTYPE html>
<html lang="en">
<head>
<meta charset="utf-8">
<title>Tip Tumble – Game Boards</title>
<link rel="stylesheet" href="https://fonts.googleapis.com/css2?family=Jost:wght@500;700&display=swap">
<style>
  :root {
    --backdrop: #5e3720;
    --orange: #fd8731;
    --orange-faint: rgba(253, 135, 49, 0.22);
    --blue: #29a3de;
    --blue-faint: rgba(41, 163, 222, 0.26);
    --paper: #ffffff;
    --divider: rgba(255, 255, 255, 0.35);
    --north-america: #45bf97;
    --south-america: #2b2b33;
    --africa: #ea2a3f;
    --eurasia: #6747b8;
    --oceania: #58d60f;
  }
  * { box-sizing: border-box; margin: 0; padding: 0; }
  html, body { width: 960px; height: 1200px; overflow: hidden; }
  body {
    background: var(--backdrop);
    font-family: "Jost", "Century Gothic", sans-serif;
    position: relative;
  }
  .board {
    position: absolute;
    display: grid;
    background: var(--paper);
    color: var(--paper);
    --line: var(--orange);
  }
  .board--full {
    left: 84px; top: 64px; width: 790px; height: 518px;
    grid-template-columns: 72px repeat(10, 1fr);
    grid-template-rows: 56px repeat(8, 1fr);
  }
  .board--wee {
    left: 85px; top: 616px; width: 789px; height: 518px;
    grid-template-columns: 79px repeat(9, 1fr);
    grid-template-rows: 65px repeat(7, 1fr);
    --line: var(--blue);
  }
  .board--full .label { background: var(--orange); }
  .board--wee .label { background: var(--blue); }
  .label {
    display: flex; align-items: center; justify-content: center;
    font-size: 44px; font-weight: 500; line-height: 1;
  }
  .label--col { border-left: 1.5px solid var(--divider); padding-top: 4px; }
  .label--row { border-top: 1.5px solid var(--divider); }
  .corner-mark span {
    width: 46px; height: 46px; border: 2px solid var(--paper); border-radius: 50%;
    display: flex; align-items: center; justify-content: center; text-align: center;
    font-size: 9px; font-weight: 700; line-height: 1.05;
  }
  .field {
    position: relative; overflow: hidden;
    grid-column: 2 / -1; grid-row: 2 / -1;
    background-image:
      linear-gradient(to right, var(--line) 1.5px, transparent 1.5px),
      linear-gradient(to bottom, var(--line) 1.5px, transparent 1.5px);
  }
  .board--full .field { background-size: calc(100% / 10) calc(100% / 8); }
  .board--wee .field { background-size: calc(100% / 9) calc(100% / 7); }
  .world-map {
    position: absolute; left: 56px; top: 62px; width: 608px; height: 338px;
    border-radius: 48px;
    background: linear-gradient(90deg,
      var(--north-america) 0%, var(--north-america) 26%,
      var(--south-america) 34%, var(--south-america) 40%,
      var(--africa) 50%, var(--africa) 56%,
      var(--eurasia) 66%, var(--eurasia) 84%,
      var(--oceania) 94%, var(--oceania) 100%);
    opacity: 0.82;
  }
  .board--wee .world-map { left: 48px; top: 51px; }
  .brand-stamp {
    position: absolute; width: 368px; height: 368px; border-radius: 50%;
    border: 26px solid var(--orange-faint);
    display: flex; align-items: center; justify-content: center;
    font-size: 54px; font-weight: 700; letter-spacing: 0.04em;
    color: var(--orange-faint); text-align: center; line-height: 1;
  }
  .board--full .brand-stamp { left: 176px; top: 46px; }
  .board--wee .brand-stamp { left: 168px; top: 39px; border-color: var(--blue-faint); color: var(--blue-faint); }
  .site-tag {
    position: absolute; bottom: 10px; left: 50%; transform: translateX(-50%);
    width: 144px; height: 13px; color: var(--paper);
    font-size: 10.5px; font-weight: 500; line-height: 13px; text-align: center;
  }
  .board--full .site-tag { background: var(--orange); }
  .board--wee .site-tag { background: var(--blue); bottom: 12px; }
</style>
</head>
<body>
  <section class="board board--full" aria-label="Tip Tumble game board, columns A to K, rows 1 to 8">
    <div class="label corner-mark"><span>Tip<br>Tumble</span></div>
    <div class="label label--col">A</div><div class="label label--col">B</div><div class="label label--col">C</div>
    <div class="label label--col">D</div><div class="label label--col">E</div><div class="label label--col">F</div>
    <div class="label label--col">G</div><div class="label label--col">I</div><div class="label label--col">J</div>
    <div class="label label--col">K</div>
    <div class="label label--row" style="grid-column:1;grid-row:2">1</div>
    <div class="label label--row" style="grid-column:1;grid-row:3">2</div>
    <div class="label label--row" style="grid-column:1;grid-row:4">3</div>
    <div class="label label--row" style="grid-column:1;grid-row:5">4</div>
    <div class="label label--row" style="grid-column:1;grid-row:6">5</div>
    <div class="label label--row" style="grid-column:1;grid-row:7">6</div>
    <div class="label label--row" style="grid-column:1;grid-row:8">7</div>
    <div class="label label--row" style="grid-column:1;grid-row:9">8</div>
    <div class="field">
      <div class="world-map" role="img" aria-label="World map with each continent in its own colour: green, black, red, purple and lime"></div>
      <div class="brand-stamp">TIP<br>TUMBLE</div>
      <div class="site-tag">TipTumble.com</div>
    </div>
  </section>

  <section class="board board--wee" aria-label="Tip a wee tumble game board, columns A to J, rows 1 to 7">
    <div class="label corner-mark"><span>Tip<br>Tumble</span></div>
    <div class="label label--col">A</div><div class="label label--col">B</div><div class="label label--col">C</div>
    <div class="label label--col">D</div><div class="label label--col">E</div><div class="label label--col">F</div>
    <div class="label label--col">G</div><div class="label label--col">I</div><div class="label label--col">J</div>
    <div class="label label--row" style="grid-column:1;grid-row:2">1</div>
    <div class="label label--row" style="grid-column:1;grid-row:3">2</div>
    <div class="label label--row" style="grid-column:1;grid-row:4">3</div>
    <div class="label label--row" style="grid-column:1;grid-row:5">4</div>
    <div class="label label--row" style="grid-column:1;grid-row:6">5</div>
    <div class="label label--row" style="grid-column:1;grid-row:7">6</div>
    <div class="label label--row" style="grid-column:1;grid-row:8">7</div>
    <div class="field">
      <div class="world-map" role="img" aria-label="World map with each continent in its own colour: green, black, red, purple and lime"></div>
      <div class="brand-stamp">TIP<br>TUMBLE</div>
      <div class="site-tag">TipTumble.com</div>
    </div>
  </section>
</body>
</html>
```